Business card design needed

play house and learning centre for toddlers and pre-schoolers, before and after school care for primary school aged children

focus on fun, bright and natural outdoor setting, art and creative play and activities
emphasis on durability, comfort and safety in facilities - child height and accessible to encourage independence, skills development and healthy interaction with others
Updates

Hi All

I will now be looking at the one-sided designs only after careful consideration.  My friends whom I have consulted on the designs have pointed out the practicalities of having all information on front page and having uncluttered blank space to write appointments or their own notes about their contact on the business card.

Please bear this in mind when submitting designs and a big  thank you for those who have taken the time to submit both two and one-sided designs.

Please note the organisation of the information on the card (without necessarily using the labels I had placed here or the font sizes which are not my settings, or the indents) as follows:

Business name: Maple Nook Tots

Tag: Family Day Care & OSH Care

Name: Lorna Bexley Whitcombe

Position Title: Registered Family Day Care Educator

ABN: 57 908 613 352

Street Address: 19 Parrow Lane New Lambton NSW 2305

Postal Address: PO Box 71 Kotara NSW 2289

Mobile: 0491 627 305

Email: lorna.b.whitcombe@mailbrook.example

Please note three changes with the information: the position title, street address and mobile phone.

Thanks.

Reason: Hi all. Just giving a little more time for final revisions and I will be opening up remaining designs to a voting poll. We're almost there!

Hi all

Tonight is the absolute deadline for my business card design project so please submit your final entries as I hope to make a decision by 8pm.  

Thanks to all those who have made submissions.  I really appreciate your ideas, creativity and efforts.  Your designs have reflected back to me the impressions that you have made from what I am trying to communicate with my business, as well as told me how well I have presented the brief.  As professionals in your field, I am sure you are aware of the importance of first impressions with business cards and I am grateful to have had this opportunity to work in this way and try out this method for the first time to achieve a great design with your participation.

Target Market(s)

parents (aged 25 - 45) of young children either high earning professionals or single income families, primary schools, toddlers and pre-schoolers

Industry/Entity Type

School

Contact Information for Business Card

Maple Nook Tots
Family Day Care & OSH Care
Lorna Bexley Whitcombe
Registered Early Childhood Carer & Educator
ABN 57 908 613 352

19 Parrow Lane New Lambton NSW
PO Box 71 Kotara NSW 2289
M: 0491 627 305
E: lorna.b.whitcombe@mailbrook.example

```html
<!DOCTYPE html>
<html lang="en">
<head>
<meta charset="utf-8">
<title>Maple Nook Tots – Business Card</title>
<link rel="stylesheet" href="https://fonts.googleapis.com/css2?family=Didact+Gothic&display=swap">
<style>
  :root {
    --backdrop: #4a4a4c;
    --card-white: #f7f7f7;
    --ink: #2b2b2b;
    --brand-navy: #2b3a8f;
    --brand-blue: #3d7fd0;
    --accent-green: #6cb52d;
    --accent-orange: #e0641e;
    --deep-blue: #23247a;
    --mid-blue: #3a63c4;
    --light-blue: #a8d6f2;
    --white: #ffffff;
  }
  * { box-sizing: border-box; margin: 0; padding: 0; }
  html, body {
    width: 1200px; height: 900px; overflow: hidden;
    background: var(--backdrop);
    font-family: "Didact Gothic", "Century Gothic", sans-serif;
  }
  .stage { position: relative; width: 1200px; height: 900px; }
  .card {
    position: absolute; left: 320px; width: 560px; height: 320px;
    box-shadow: 0 10px 30px rgba(0,0,0,.35);
  }
  /* Front */
  .card--front { top: 110px; background: var(--card-white); color: var(--ink); }
  .brand { position: absolute; display: flex; align-items: center; gap: 10px; }
  .card--front .brand { left: 170px; top: 48px; }
  .brand__dot { width: 16px; height: 16px; border-radius: 50%; background: var(--accent-orange); }
  .brand__name { font-size: 30px; color: var(--brand-navy); letter-spacing: .2px; }
  .card--front .tagline { position: absolute; left: 196px; top: 92px; font-size: 14px; color: var(--brand-navy); }
  .person { position: absolute; right: 40px; top: 140px; text-align: right; }
  .person__name { font-size: 20px; }
  .person__role { font-size: 12.5px; color: var(--accent-green); margin-top: 4px; }
  .contact { position: absolute; left: 40px; top: 222px; font-size: 14.5px; line-height: 1.45; }
  .contact__label { color: var(--accent-green); }
  .abn { position: absolute; right: 40px; bottom: 30px; font-size: 14.5px; }
  /* Back */
  .card--back {
    top: 470px;
    background: radial-gradient(ellipse 70% 90% at 82% 62%, var(--light-blue) 0%, var(--mid-blue) 55%, var(--deep-blue) 100%);
    color: var(--white);
  }
  .card--back .brand { left: 40px; top: 96px; }
  .card--back .brand__name { color: var(--white); font-size: 42px; }
  .card--back .brand__dot { width: 20px; height: 20px; }
  .card--back .tagline { position: absolute; left: 40px; top: 156px; font-size: 20px; color: var(--white); }
  .motto { position: absolute; right: 40px; bottom: 40px; text-align: right; font-size: 17px; line-height: 1.25; }
</style>
</head>
<body>
<main class="stage">
  <section class="card card--front" aria-label="Business card front">
    <div class="brand"><span class="brand__dot"></span><span class="brand__name">Maple Nook Tots</span></div>
    <p class="tagline">Family Day Care &amp; OSH Care</p>
    <div class="person">
      <p class="person__name">Lorna Bexley Whitcombe</p>
      <p class="person__role">Registered Early Childhood Carer &amp; Educator</p>
    </div>
    <div class="contact">
      <p>19 Parrow Lane New Lambton NSW &nbsp;| PO Box 71 Kotara NSW 2289</p>
      <p><span class="contact__label">M:</span> 0491 627 305 | <span class="contact__label">E:</span> lorna.b.whitcombe@mailbrook.example</p>
    </div>
    <p class="abn">ABN 57 908 613 352</p>
  </section>

  <section class="card card--back" aria-label="Business card back">
    <div class="brand"><span class="brand__dot"></span><span class="brand__name">Maple Nook Tots</span></div>
    <p class="tagline">Family Day Care &amp; OSH Care</p>
    <p class="motto">play house and learning centre<br>for toddlers and pre-schooler</p>
  </section>
</main>
</body>
</html>
```